Cardiology practice business card

We need a business card for our cardiology practice "Bellmoor Cardiology". We have a new logo, attached below. We like the colours in the logo - red and charcoal. The front of the business card will need to have the doctors name, address, phone number and email. The back will need to have space to write 2 appointment dates and times.

```html
<!DOCTYPE html>
<html lang="en">
<head>
<meta charset="utf-8">
<title>Bellmoor Cardiology – Business Card</title>
<link rel="stylesheet" href="https://fonts.googleapis.com/css2?family=Playfair+Display:wght@400;700&display=swap">
<style>
  :root {
    --backdrop: #e7e1de;
    --card: #f6f3f1;
    --red: #d6373b;
    --charcoal: #5a5a5a;
    --ink: #6d6d6d;
    --rule: #b9b3b0;
    --shadow: rgba(60, 40, 35, 0.18);
  }
  * { box-sizing: border-box; margin: 0; padding: 0; }
  html, body {
    width: 1200px; height: 768px; overflow: hidden;
    background: var(--backdrop);
    font-family: "Playfair Display", Georgia, serif;
  }
  .sheet {
    position: relative; width: 1200px; height: 768px;
    display: flex; justify-content: center; align-items: center; gap: 40px;
  }
  .card {
    position: relative; width: 520px; height: 297px;
    background: var(--card);
    box-shadow: 0 10px 30px var(--shadow);
  }
  .brand {
    display: flex; align-items: center; gap: 10px;
    color: var(--red); font-weight: 700; letter-spacing: 0.02em;
    white-space: nowrap;
  }
  .brand-dot {
    width: 12px; height: 12px; border-radius: 50%; background: var(--red); flex: none;
  }

  /* Back: brand + appointment slots */
  .card-back {
    display: flex; flex-direction: column; align-items: center;
    justify-content: center; gap: 30px;
  }
  .card-back .brand { font-size: 28px; }
  .appointments { list-style: none; width: 400px; }
  .appointment {
    display: flex; align-items: flex-end; gap: 8px;
    color: var(--charcoal); font-size: 12px; letter-spacing: 0.04em;
    text-transform: uppercase; line-height: 1; margin-top: 18px;
  }
  .appointment .blank {
    flex: 1; border-bottom: 1px solid var(--rule); height: 12px;
  }
  .appointment .blank-date { flex: 1.4; }

  /* Front: contact details */
  .card-front .edge {
    position: absolute; height: 3px; background: var(--red);
  }
  .edge-top { top: 0; left: 0; width: 62%; }
  .edge-bottom { bottom: 0; right: 0; width: 62%; }
  .divider {
    position: absolute; left: 42%; top: 22%; width: 4px; height: 68%;
    background: var(--charcoal);
  }
  .card-front .brand {
    position: absolute; left: 20px; top: 150px; gap: 8px;
    font-size: 15px;
  }
  .card-front .brand-dot { width: 8px; height: 8px; }
  .details {
    position: absolute; left: 49%; top: 22%; right: 18px;
  }
  .person-name {
    color: var(--red); font-size: 22px; font-weight: 700;
    text-transform: uppercase; letter-spacing: 0.02em;
  }
  .person-role {
    color: var(--charcoal); font-size: 18px; font-weight: 700;
    margin-top: 2px;
  }
  .address {
    margin-top: 16px; color: var(--ink); font-size: 10.5px;
    text-transform: uppercase; letter-spacing: 0.06em; line-height: 1.45;
  }
  .contact-list { list-style: none; margin-top: 8px; }
  .contact-list li {
    display: flex; align-items: center; gap: 10px;
    color: var(--ink); font-size: 11px; letter-spacing: 0.03em;
    line-height: 1.9;
  }
  .contact-list svg { width: 13px; height: 13px; flex: none; }
</style>
</head>
<body>
<main class="sheet">
  <section class="card card-back">
    <div class="brand"><span class="brand-dot"></span><span>Bellmoor Cardiology</span></div>
    <ul class="appointments">
      <li class="appointment"><span>Date</span><span class="blank blank-date"></span><span>Time</span><span class="blank"></span></li>
      <li class="appointment"><span>Date</span><span class="blank blank-date"></span><span>Time</span><span class="blank"></span></li>
    </ul>
  </section>

  <section class="card card-front">
    <span class="edge edge-top"></span>
    <span class="edge edge-bottom"></span>
    <div class="brand"><span class="brand-dot"></span><span>Bellmoor Cardiology</span></div>
    <span class="divider"></span>
    <div class="details">
      <h1 class="person-name">Elena Marsh</h1>
      <p class="person-role">owner</p>
      <p class="address">48 Harbour view lane suite 12<br>Bellmoor 4870</p>
      <ul class="contact-list">
        <li>
          <svg viewBox="0 0 16 16" fill="none" stroke="var(--red)" stroke-width="1.4"><rect x="1.5" y="3.5" width="13" height="9" rx="1"/><path d="M2 4.5l6 4.5 6-4.5"/></svg>
          <span>info@bellmoorheart.com</span>
        </li>
        <li>
          <svg viewBox="0 0 16 16" fill="none" stroke="var(--red)" stroke-width="1.4"><path d="M3 2.5l2.5-.5 1.5 3-1.5 1.2a8 8 0 0 0 4.3 4.3L11 9l3 1.5-.5 2.5c-6 .5-11-4.5-10.5-10.5z"/></svg>
          <span>+070 6312 40987</span>
        </li>
        <li>
          <svg viewBox="0 0 16 16" fill="none" stroke="var(--red)" stroke-width="1.3"><circle cx="8" cy="8" r="6.5"/><ellipse cx="8" cy="8" rx="3" ry="6.5"/><path d="M1.5 8h13"/></svg>
          <span>www.bellmoorheart.com</span>
        </li>
      </ul>
    </div>
  </section>
</main>
</body>
</html>
```